Birch Flooring Supply

Basic one-sided business card design using the attached logo. Vintage americana theme. Font is modified Arial Nova Cond, but anything that coordinates can be used

```html
<!DOCTYPE html>
<html lang="en">
<head>
<meta charset="utf-8">
<title>Birch Flooring Supply – Business Card</title>
<link rel="stylesheet" href="https://fonts.googleapis.com/css2?family=Roboto+Condensed:wght@400;700&display=swap">
<style>
  :root {
    --backdrop: #d6d6d6;
    --card: #050607;
    --gold: #b39573;
    --ink: #f2f0ec;
  }
  * { box-sizing: border-box; margin: 0; padding: 0; }
  html, body {
    width: 1200px;
    height: 846px;
    overflow: hidden;
    background: var(--backdrop);
    font-family: "Roboto Condensed", "Arial Narrow", sans-serif;
  }
  .card {
    position: absolute;
    left: 394px;
    top: 63px;
    width: 412px;
    height: 720px;
    background: var(--card);
    border-radius: 206px 206px 40px 40px / 190px 190px 40px 40px;
    box-shadow: 0 8px 18px rgba(0,0,0,0.25);
  }
  .frame-outer {
    position: absolute;
    inset: 26px;
    border: 2px solid var(--gold);
    border-radius: 180px 180px 26px 26px / 166px 166px 26px 26px;
  }
  .frame-inner {
    position: absolute;
    inset: 5px;
    border: 1px solid var(--gold);
    border-radius: 175px 175px 21px 21px / 161px 161px 21px 21px;
  }
  .brand {
    position: absolute;
    top: 140px;
    left: 0;
    right: 0;
    text-align: center;
    color: var(--ink);
    font-weight: 700;
    font-size: 40px;
    line-height: 1.05;
    letter-spacing: 2px;
    text-transform: uppercase;
  }
  .details {
    position: absolute;
    top: 365px;
    left: 53px;
    right: 53px;
    text-align: center;
    color: var(--ink);
    font-weight: 700;
  }
  .person-name {
    font-size: 28px;
    letter-spacing: 0.5px;
    text-transform: uppercase;
    padding-bottom: 6px;
  }
  .rule {
    height: 1px;
    background: var(--gold);
    margin: 4px 0;
  }
  .contact-block {
    font-size: 20px;
    line-height: 28px;
    padding: 4px 0 3px;
  }
  .contact-block .phone { text-transform: uppercase; }
  .stars {
    position: absolute;
    left: 0;
    right: 0;
    top: 613px;
    display: flex;
    justify-content: center;
    gap: 19px;
  }
  .stars svg { width: 35px; height: 33px; fill: var(--gold); }
</style>
</head>
<body>
  <div class="card">
    <div class="frame-outer"><div class="frame-inner"></div></div>

    <div class="brand">Birch<br>Flooring Supply</div>

    <div class="details">
      <div class="person-name">Name Lastname</div>
      <div class="rule"></div>
      <div class="contact-block">
        <div class="phone">Phone: +1 555-014-2290</div>
        <div class="email">socials@birchflooringsupply.com</div>
      </div>
      <div class="rule"></div>
      <div class="contact-block">
        <div>1420 Elm Ave, Brookdale, MN,</div>
        <div>United States, Minnesota</div>
      </div>
      <div class="rule"></div>
      <div class="contact-block">
        <div class="web">www.birchflooringsupply.com</div>
      </div>
    </div>

    <div class="stars" aria-label="Five stars">
      <svg viewBox="0 0 24 23"><polygon points="12,0 14.8,8.6 24,8.6 16.6,14 19.4,23 12,17.5 4.6,23 7.4,14 0,8.6 9.2,8.6"/></svg>
      <svg viewBox="0 0 24 23"><polygon points="12,0 14.8,8.6 24,8.6 16.6,14 19.4,23 12,17.5 4.6,23 7.4,14 0,8.6 9.2,8.6"/></svg>
      <svg viewBox="0 0 24 23"><polygon points="12,0 14.8,8.6 24,8.6 16.6,14 19.4,23 12,17.5 4.6,23 7.4,14 0,8.6 9.2,8.6"/></svg>
      <svg viewBox="0 0 24 23"><polygon points="12,0 14.8,8.6 24,8.6 16.6,14 19.4,23 12,17.5 4.6,23 7.4,14 0,8.6 9.2,8.6"/></svg>
      <svg viewBox="0 0 24 23"><polygon points="12,0 14.8,8.6 24,8.6 16.6,14 19.4,23 12,17.5 4.6,23 7.4,14 0,8.6 9.2,8.6"/></svg>
    </div>
  </div>
</body>
</html>
```